NEW Website DESIGN for Glass & Solid Surfaces Company

Brand New website, contemporary, clean, visual (images), not busy. ATTACHED IS OUR LOG THAT YOU MUST USE.

The company is called Brightwell Panes & Stoneworks (BrightwellPS)
www.brightwellps.com
The website should be www.brightwellpns.com
one page for glass one page for solid surfaces www.brightwellpanesplashes.co.uk
www.brightwellstoneworkss.co.uk

Target Market(s)

Hotels, Commercial projects, Small focus on residential

Industry/Entity Type

Construction

Number of Pages Required

5+ page

Font styles to use
Sans Serif

Requirements
Must have
• COLOURS AS PER OUR LOGO - WHITE/YELLOW/GREY - WHITE BACK GROUND
• CLEAR SIMPLE NAVIGATION - MODER CLEAN CUT - DESIGN FEEL
• LATEST NAVIGATION FOR IMAGES and text to include per project details
• WORK/PROJECT AREA - NEWS AREA - TEAM AREA/ABOUT US/CONTACT US
• NEW PAGEwww.brightwellpanesplashes.co.uk - NEW PAGE www.brightwellstoneworkss.co.uk
• PLEASE COPY THIS TYPE OF TEMPALTE
• https://www.harlowmead.co.uk/project/grand-halls/
• MOBILE READY
• WORDPRESS
• MODERN IMAGES INCLUDING VELMARA KESTRIN AND GLASS PROJECTS
Nice to have
• NEW DESIGN MODER FRESH
• WEBSITES I LIKE THE TEMPLATE SHOULD BE LIKE THE WEBSITE BELOW
• https://www.harlowmead.co.uk/
Should not have
• NOT Old fashion template, not busy NAVIGATION
• NO BLACK
• NO DARK GREYS
• NOT LOTS OF YELLOW
• RESDENTIAL IMAGES

```html
<!DOCTYPE html>
<html lang="en">
<head>
<meta charset="utf-8">
<title>Brightwell Panes &amp; Stoneworks</title>
<link href="https://fonts.googleapis.com/css2?family=Lato:wght@400;700;900&family=Roboto:wght@400;500;700&display=swap" rel="stylesheet">
<style>
:root{
  --yellow:#dcd81c;
  --white:#ffffff;
  --ink:#222222;
  --text:#555555;
  --muted:#777777;
  --panel:#6e6e6e;
  --ghost:#ececec;
  --footer:#ececec;
  --social:#2fb5e6;
}
*{margin:0;padding:0;box-sizing:border-box}
html,body{width:1200px;height:3056px;overflow:hidden;background:var(--white)}
body{position:relative;font-family:'Roboto',sans-serif;color:var(--text)}
.abs{position:absolute}
.photo{position:absolute}

/* hero */
.hero{left:0;top:0;width:1200px;height:550px;background:linear-gradient(120deg,#5a4330 0%,#8a6a4a 35%,#c9a57c 55%,#6b5644 80%,#3c3a38 100%)}
.brand{left:60px;top:28px;width:210px;text-align:center;color:var(--white)}
.brand-mark{width:58px;height:58px;border-radius:50%;background:var(--white);margin:0 auto 8px}
.brand-name{font:700 12px 'Roboto',sans-serif}
.nav{left:516px;top:62px;display:flex;gap:0}
.nav a{color:var(--white);text-decoration:none;font:700 13px 'Roboto',sans-serif;margin-right:38px}
.nav svg{margin-top:-1px}
.hero-title{right:100px;top:296px;font:700 48px 'Lato',sans-serif;color:var(--white);text-shadow:0 2px 6px rgba(0,0,0,.35)}
.stats{right:100px;top:374px;display:flex;gap:40px;color:var(--white);text-align:right}
.stats dt{font:400 15px 'Roboto',sans-serif;margin-bottom:10px}
.stats dd{font:700 17px 'Roboto',sans-serif}

/* surface panels */
.surface{top:550px;width:600px;height:357px;color:var(--white)}
.surface-glass{left:0;background:linear-gradient(135deg,#9aa3a6,#d8d4cc 45%,#7c705f)}
.surface-solid{left:600px;background:linear-gradient(135deg,#4b4540,#c8b9a4 50%,#2f2c2a)}
.surface h2{position:absolute;left:96px;top:208px;font:700 34px 'Lato',sans-serif;text-shadow:0 2px 5px rgba(0,0,0,.4)}
.surface-solid h2{left:62px}
.surface p{position:absolute;left:96px;top:258px;width:370px;font:400 16px/21px 'Roboto',sans-serif;text-shadow:0 1px 3px rgba(0,0,0,.5)}
.surface-solid p{left:62px}

/* about */
.ghost{font:900 72px 'Lato',sans-serif;color:var(--ghost);letter-spacing:1px;white-space:nowrap}
.about-box{left:508px;top:907px;width:592px;height:335px;border:3px solid var(--yellow);background:var(--white)}
.about-box h2{position:absolute;left:0;right:0;top:44px;text-align:center;font:700 36px 'Lato',sans-serif;color:var(--ink)}
.about-box p{position:absolute;left:122px;width:436px;top:110px;text-align:center;font:400 12px/25px 'Roboto',sans-serif;color:var(--muted)}
.btn{position:absolute;left:267px;top:240px;width:151px;height:40px;border:1px solid #444;border-radius:3px;font:700 13px 'Roboto',sans-serif;color:var(--ink);display:flex;align-items:center;justify-content:center;gap:4px}
.about-photo{left:98px;top:1035px;width:502px;height:530px;background:linear-gradient(160deg,#d9d4cb,#a89a88 45%,#6a4a2e 85%)}
.project-panel{left:508px;top:1348px;width:592px;height:217px;background:var(--panel);color:var(--white)}
.project-panel h3{position:absolute;left:24px;top:44px;font:700 26px 'Lato',sans-serif}
.project-panel .rule{position:absolute;left:24px;top:94px;width:88px;height:2px;background:var(--yellow)}
.project-panel p{position:absolute;left:24px;top:110px;width:540px;font:400 12px/24px 'Roboto',sans-serif}
.project-panel .arrows{position:absolute;right:26px;top:180px;display:flex;gap:14px}

/* testimonials */
.testimonials{left:0;top:1676px;width:1200px;height:474px;background:linear-gradient(120deg,#8a7a64,#cbb894 40%,#b8a27e 65%,#6f6050)}
.testimonials .shade{position:absolute;inset:0;background:rgba(60,45,30,.28)}
.ghost-light{font:900 72px 'Lato',sans-serif;color:rgba(255,255,255,.28);white-space:nowrap}
.testimonials h2{position:absolute;left:0;right:0;top:76px;text-align:center;font:700 34px 'Lato',sans-serif;color:var(--white)}
.avatar{position:absolute;left:560px;top:152px;width:80px;height:80px;border-radius:50%;background:#c9d3df;border:3px solid var(--white)}
.quote{position:absolute;left:200px;width:800px;top:250px;text-align:center;font:700 16px/29px 'Roboto',sans-serif;color:var(--white)}
.cite{position:absolute;left:0;right:0;top:330px;text-align:center;font:400 13px 'Roboto',sans-serif;color:var(--white)}
.cite b{font-weight:700}
.stars{position:absolute;left:555px;top:364px;width:90px;height:22px;background:var(--yellow);display:flex;align-items:center;justify-content:center;gap:2px}
.tarrow{position:absolute;top:248px}

/* latest project */
.latest h2{position:absolute;left:0;right:0;top:2230px;text-align:center;font:700 34px 'Lato',sans-serif;color:var(--ink)}
.card{top:2327px;width:312px}
.card .thumb{height:213px;border:4px solid #f1f1f1}
.card h3{margin-top:42px;font:700 19px 'Lato',sans-serif;color:var(--ink)}
.card p{margin-top:18px;font:400 12px/23px 'Roboto',sans-serif;color:var(--muted)}
.card a{display:inline-flex;align-items:center;gap:6px;margin-top:16px;font:500 12px 'Roboto',sans-serif;color:var(--yellow);text-decoration:underline}

/* footer */
.footer{left:0;top:2812px;width:1200px;height:244px;background:var(--footer)}
.socials{position:absolute;left:0;right:0;top:76px;display:flex;justify-content:center;gap:12px}
.socials span{width:38px;height:38px;border-radius:50%;border:2px solid #555}
.socials span.on{background:var(--social);border-color:var(--social)}
.copyright{position:absolute;left:0;right:0;top:140px;text-align:center;font:400 15px 'Roboto',sans-serif;color:var(--text)}
.legal{position:absolute;left:0;right:0;top:178px;text-align:center;font:400 13px 'Roboto',sans-serif;color:var(--text)}
.legal i{font-style:normal;margin:0 14px}
</style>
</head>
<body>

<header class="photo hero" role="img" aria-label="Warm wood-panelled hotel bathroom with floating white basin, lit mirror and glass shower"></header>
<div class="abs brand">
  <div class="brand-mark"></div>
  <div class="brand-name">Brightwell Panes &amp; Stoneworks</div>
</div>
<nav class="abs nav">
  <a>HOME</a><a>PROJECTS</a><a>NEWS</a><a>TEAM</a><a>ABOUT US</a><a>CONTACT US</a>
  <svg width="14" height="14" viewBox="0 0 14 14"><circle cx="6" cy="6" r="4.5" fill="none" stroke="#fff" stroke-width="2"/><line x1="9.2" y1="9.2" x2="13" y2="13" stroke="#fff" stroke-width="2"/></svg>
</nav>
<h1 class="abs hero-title">Glass Surfaces Room</h1>
<dl class="abs stats">
  <div><dt>Value</dt><dd>$18.98 million</dd></div>
  <div><dt>Rooms</dt><dd>14</dd></div>
  <div><dt>Duration</dt><dd>26 weeks</dd></div>
</dl>

<section class="abs surface surface-glass" role="img" aria-label="Bright bathroom with frameless glass shower enclosure and vessel basin">
  <h2>Glass Surface</h2>
  <p>Nam libero tempore, cum soluta est eligendi optio cumque nihil impedit minus.</p>
</section>
<section class="abs surface surface-solid" role="img" aria-label="Modern bathroom with solid surface vanity top and wall mirror">
  <h2>Solid Surface</h2>
  <p>Nam libero tempore, cum soluta est eligendi optio cumque nihil impedit minus.</p>
</section>

<div class="abs ghost" style="left:22px;top:925px">ABOUT US</div>
<div class="photo about-photo" role="img" aria-label="Bathroom vanity with stone worktop, twin bowl basins and large mirror"></div>
<section class="abs about-box">
  <h2>ABOUT US</h2>
  <p>Nam libero tempore, cum soluta nobis est eligendi optio cumque nihil minus id quod maxime placeat facere possimus, omnis voluptas assumenda est, omnis dolor repellendus. Temporibus autem quibusdam aut officiis debitis aut rerum necessitatibus saepe eveniet ut et..</p>
  <div class="btn">READ MORE <svg width="11" height="11" viewBox="0 0 12 12"><circle cx="6" cy="6" r="6" fill="#222"/><path d="M5 3l3 3-3 3" stroke="#fff" stroke-width="1.6" fill="none"/></svg></div>
</section>
<section class="abs project-panel">
  <h3>New Home Project</h3>
  <div class="rule"></div>
  <p>Nam libero tempore, cum soluta nobis est eligendi optio cumque nihil impedit quo minus id quod maxime placeat facere possimus, omnis voluptas assumenda est</p>
  <div class="arrows">
    <svg width="8" height="14" viewBox="0 0 8 14"><path d="M7 1L1 7l6 6" stroke="#fff" stroke-width="1.8" fill="none"/></svg>
    <svg width="8" height="14" viewBox="0 0 8 14"><path d="M1 1l6 6-6 6" stroke="#fff" stroke-width="1.8" fill="none"/></svg>
  </div>
</section>

<section class="abs testimonials" role="img" aria-label="Classic bathroom with stone bath surround, framed mirror and glass block window">
  <div class="shade"></div>
  <div class="abs ghost-light" style="left:352px;top:54px">TESTIMONIALS</div>
  <h2>WHAT OUR CLIENTS SAY?</h2>
  <div class="avatar" role="img" aria-label="Client portrait"></div>
  <p class="quote">" Nemo enim ipsam voluptatem quia voluptas sit aspernatur aut odit aut fugit quia consequuntur magni dolores eos qui ratione voluptatem nesciunt porro dolorem ipsum "</p>
  <p class="cite"><b>MARLA QUENBY,</b> Director of Manager</p>
  <div class="stars">
    <svg width="80" height="14" viewBox="0 0 80 14"><g fill="#8a6d00"><path id="s" d="M7 0l2 4.6 5 .5-3.8 3.3 1.1 4.9L7 10.8 2.7 13.3l1.1-4.9L0 5.1l5-.5z"/><use href="#s" x="16"/><use href="#s" x="32"/><use href="#s" x="48"/><use href="#s" x="64"/></g></svg>
  </div>
  <svg class="tarrow" style="left:80px" width="16" height="28" viewBox="0 0 16 28"><path d="M14 2L3 14l11 12" stroke="#fff" stroke-width="3" fill="none"/></svg>
  <svg class="tarrow" style="left:1104px" width="16" height="28" viewBox="0 0 16 28"><path d="M2 2l11 12L2 26" stroke="#fff" stroke-width="3" fill="none"/></svg>
</section>

<section class="latest">
  <div class="abs ghost" style="left:325px;top:2210px">LATEST PROJECT</div>
  <h2>OUR LATEST PROJECT</h2>
  <article class="abs card" style="left:98px">
    <div class="thumb" role="img" aria-label="Vanity with white basin, marble top and timber splashback" style="background:linear-gradient(180deg,#5a3a2a,#7a5440 50%,#d8d2cc)"></div>
    <h3>Discover Undoubtable Source</h3>
    <p>Nam libero tempore, cum soluta nobis est eligendi optio cumque nihil impedit quo minus id quod ma ixime placeat facere possimus</p>
    <a>READ MORE <svg width="11" height="11" viewBox="0 0 12 12"><circle cx="6" cy="6" r="6" fill="#dcd81c"/><path d="M5 3l3 3-3 3" stroke="#fff" stroke-width="1.6" fill="none"/></svg></a>
  </article>
  <article class="abs card" style="left:443px">
    <div class="thumb" role="img" aria-label="Bathroom with glass block wall and fitted bath" style="background:linear-gradient(135deg,#6a4e36,#c9a77f 50%,#8c6a48)"></div>
    <h3>Discover Undoubtable Source</h3>
    <p>Nam libero tempore, cum soluta nobis est eligendi optio cumque nihil impedit quo minus id quod ma ixime placeat facere possimus</p>
    <a>READ MORE <svg width="11" height="11" viewBox="0 0 12 12"><circle cx="6" cy="6" r="6" fill="#dcd81c"/><path d="M5 3l3 3-3 3" stroke="#fff" stroke-width="1.6" fill="none"/></svg></a>
  </article>
  <article class="abs card" style="left:790px">
    <div class="thumb" role="img" aria-label="Grey tiled bathroom with glass shower and wall-hung basin" style="background:linear-gradient(135deg,#4a4a4a,#bdbdbd 50%,#3a3a3a)"></div>
    <h3>Discover Undoubtable Source</h3>
    <p>Nam libero tempore, cum soluta nobis est eligendi optio cumque nihil impedit quo minus id quod ma ixime placeat facere possimus</p>
    <a>READ MORE <svg width="11" height="11" viewBox="0 0 12 12"><circle cx="6" cy="6" r="6" fill="#dcd81c"/><path d="M5 3l3 3-3 3" stroke="#fff" stroke-width="1.6" fill="none"/></svg></a>
  </article>
</section>

<footer class="abs footer">
  <div class="socials"><span></span><span class="on"></span><span></span><span></span></div>
  <p class="copyright">© Copyright 2018 Brightwell Panes &amp; Stoneworks. All Rights Reserved.</p>
  <p class="legal">FAQ<i>|</i>Privacy Policy<i>|</i>Terms &amp; Conditions</p>
</footer>

</body>
</html>
```